MOLVT Study flyer

I need help designing a flyer for a research study that will include brain imaging in adolescents. The info is in the attached document. The study is called the Marrowby Orchard Lantern Vesper Trail (MOLVT) study. Ideally this would be returned as a document that I can edit in the future as we will have several new recruitment phases (different age groups, etc. I also would love to have a logo designed as part of this project, but I recognize that might be a separate design request.

```html
<!DOCTYPE html>
<html lang="en">
<head>
<meta charset="utf-8">
<title>MOLVT Study Flyer</title>
<link href="https://fonts.googleapis.com/css2?family=Bebas+Neue&family=Poppins:ital,wght@0,400;0,500;0,600;0,700;1,700&family=Playball&display=swap" rel="stylesheet">
<style>
:root{
  --navy:#2c2470;
  --lavender:#8a68b8;
  --lavender-soft:#d9d0ea;
  --teal:#178a86;
  --teal-dark:#0f6f6c;
  --ink:#2b2a4a;
  --panel:#e8e9ef;
  --stage:#a6a7aa;
  --white:#ffffff;
}
*{box-sizing:border-box;margin:0;padding:0}
html,body{width:1200px;height:3656px;overflow:hidden}
body{background:var(--stage);font-family:"Poppins",sans-serif;color:var(--ink);position:relative}
.flyer{position:absolute;left:60px;top:1063px;width:1080px;height:1529px;background:var(--white);overflow:hidden}
.abs{position:absolute}

/* header */
.brand{left:50px;top:60px;display:flex;align-items:center;gap:22px}
.brand-dot{width:118px;height:118px;border-radius:50%;background:var(--lavender)}
.brand-name{font-family:"Bebas Neue",sans-serif;font-size:82px;line-height:.9;color:var(--navy)}
.brand-sub{font-size:13px;font-weight:500;color:var(--lavender);line-height:1.3;width:190px;border-bottom:3px solid var(--teal);padding-bottom:6px;margin-top:4px}

.photo{left:560px;top:0;width:520px;height:705px;background:linear-gradient(180deg,#f1eef7 0%,#e4dcef 40%,#b9a2dc 68%,#8a68b8 82%,#3b4f7c 100%)}

.headline{left:66px;top:222px;font-family:"Bebas Neue",sans-serif;font-size:82px;line-height:.95;color:var(--navy)}
.headline .accent{color:var(--teal)}
.subhead{left:66px;top:400px;font-size:35px;font-weight:600;line-height:1.15;color:var(--lavender)}

.intro-band{left:0;top:532px;width:830px;height:173px;background:var(--navy);display:flex;align-items:center}
.intro-band svg{margin-left:52px;flex:none}
.intro-band p{color:var(--white);font-size:20px;font-weight:500;line-height:1.3;margin-left:48px;width:430px}
.intro-band em{font-weight:700}

.pay{left:828px;top:496px;width:252px;height:252px;border-radius:50%;background:var(--teal);border:8px solid var(--white);box-shadow:0 0 0 4px var(--teal);text-align:center;color:var(--white);padding-top:38px}
.pay small{display:block;font-size:20px;line-height:1.15}
.pay strong{display:block;font-family:"Bebas Neue",sans-serif;font-size:112px;line-height:1;margin-top:4px}

/* participation */
.section-title{left:0;top:720px;width:1080px;display:flex;align-items:center;gap:20px;font-size:26px;font-weight:700;color:var(--navy)}
.section-title::before{content:"";height:2px;width:280px;background:var(--navy)}
.section-title::after{content:"";height:2px;flex:1;background:var(--navy);margin-right:40px}

.steps{left:60px;top:770px;width:960px;display:flex}
.step{flex:1;text-align:center;padding:0 20px}
.step + .step{border-left:2px dashed #c9c9d4}
.step-icon{width:104px;height:104px;border-radius:50%;margin:0 auto 14px;display:flex;align-items:center;justify-content:center}
.step-title{font-size:19px;font-weight:600;line-height:1.2}
.step-note{font-size:15px;line-height:1.2;margin-top:4px}
.step.navy .step-icon{background:var(--navy)} .step.navy .step-title{color:var(--navy)}
.step.teal .step-icon{background:var(--teal)} .step.teal .step-title{color:var(--teal)}
.step.lav .step-icon{background:var(--lavender)} .step.lav .step-title{color:var(--lavender)}
.step.lav .step-note{text-align:left}

/* eligibility */
.eligible{left:48px;top:1042px;width:985px;height:195px;background:var(--panel);border-radius:18px;overflow:hidden}
.eligible h3{position:absolute;left:32px;top:28px;font-size:23px;font-weight:700;color:var(--navy)}
.eligible ul{position:absolute;left:32px;top:72px;list-style:none;width:500px}
.eligible li{display:flex;gap:14px;font-size:18px;line-height:1.2;margin-bottom:8px}
.eligible li svg{flex:none;margin-top:2px}
.scan{position:absolute;right:0;top:0;width:446px;height:195px;border-radius:18px;background:linear-gradient(120deg,#1e4d8f 0%,#5ea9e6 45%,#cfe8fb 60%,#2b5fa8 100%)}

/* contact */
.contact{left:48px;top:1267px;width:985px;height:88px;background:var(--teal);border-radius:10px;display:flex;align-items:center}
.contact-label{font-family:"Playball",cursive;font-size:40px;color:var(--white);padding:0 28px;width:344px;background:var(--teal-dark);height:100%;display:flex;align-items:center;border-radius:10px 0 0 10px;white-space:nowrap}
.contact-ask{color:var(--white);font-size:17px;line-height:1.2;margin-left:24px;width:290px}
.contact-mail{margin-left:auto;margin-right:20px;background:var(--white);border-radius:6px;height:52px;padding:0 16px;display:flex;align-items:center;gap:12px;font-size:17px;font-weight:500;color:var(--teal);white-space:nowrap}

/* footer */
.footer{left:0;top:1387px;width:1080px;height:142px;background:var(--navy);display:flex;align-items:center}
.org{display:flex;align-items:center;gap:18px;margin-left:64px;width:380px;color:var(--white);font-size:30px;font-weight:500;line-height:1.05;flex:none}
.org-mark{width:58px;height:58px;background:var(--white);flex:none}
.footer-rule{width:2px;height:70px;background:var(--white);flex:none}
.url{color:var(--white);font-size:30px;font-weight:600;margin-left:44px;white-space:nowrap}
</style>
</head>
<body>
<main class="flyer">
  <div class="photo abs" role="img" aria-label="Photo of a thoughtful teenage girl in a lavender sweater, chin on hand, with faint brain-network graphics and a thought bubble behind her"></div>

  <div class="brand abs">
    <div class="brand-dot"></div>
    <div>
      <div class="brand-name">MOLVT</div>
      <div class="brand-sub">MARROWBY ORCHARD LANTERN VESPER TRAIL STUDY</div>
    </div>
  </div>

  <h1 class="headline abs">ARE YOU THE PARENT<br>OF <span class="accent">A CHILD AGE 10-17?</span></h1>
  <h2 class="subhead abs">DO THEY WORRY OR<br>OVERTHINK NEGATIVE<br>EMOTIONS?</h2>

  <section class="intro-band abs">
    <svg width="110" height="120" viewBox="0 0 110 120" fill="none" stroke="#fff" stroke-width="2.5" aria-hidden="true">
      <path d="M30 112V92c-14-8-22-22-22-40C8 26 28 8 54 8s46 18 46 42c0 8-3 14-4 18l8 14-9 3v12c0 6-5 9-11 9H70v6"/>
      <circle cx="44" cy="44" r="10"/><circle cx="64" cy="40" r="12"/><circle cx="56" cy="60" r="10"/><circle cx="38" cy="62" r="8"/>
    </svg>
    <p>Halvern Ridge University researchers are seeking <em>girls age 10-17</em> for a study about brain activity in emotions and decision-making and how they relate to puberty, anxiety and depression.</p>
  </section>

  <div class="pay abs"><small>Compensation<br>up to</small><strong>$140</strong></div>

  <div class="section-title abs">STUDY PARTICIPATION INVOLVES</div>

  <section class="steps abs">
    <div class="step navy">
      <div class="step-icon">
        <svg width="56" height="56" viewBox="0 0 56 56" fill="none" stroke="#fff" stroke-width="2.5" aria-hidden="true"><rect x="4" y="4" width="18" height="12" rx="2"/><rect x="34" y="4" width="18" height="12" rx="2"/><circle cx="16" cy="28" r="5"/><circle cx="40" cy="28" r="5"/><path d="M6 50c0-8 4-12 10-12s10 4 10 12M30 50c0-8 4-12 10-12s10 4 10 12"/></svg>
      </div>
      <div class="step-title">ONE ONE-HOUR<br>INTERVIEW</div>
      <div class="step-note">(online or in-person)<br>where your child will<br>discuss their thoughts</div>
    </div>
    <div class="step teal">
      <div class="step-icon">
        <svg width="56" height="56" viewBox="0 0 56 56" fill="none" stroke="#fff" stroke-width="2.5" aria-hidden="true"><rect x="6" y="6" width="44" height="32" rx="3"/><path d="M20 46h16M28 38v8M14 16l3 3 5-5M26 17h16M14 28l3 3 5-5M26 29h16"/></svg>
      </div>
      <div class="step-title">ONLINE<br>QUESTIONNAIRES</div>
      <div class="step-note">(parent and child)</div>
    </div>
    <div class="step lav">
      <div class="step-icon">
        <svg width="56" height="56" viewBox="0 0 56 56" fill="none" stroke="#fff" stroke-width="2.5" aria-hidden="true"><circle cx="28" cy="24" r="16"/><circle cx="28" cy="24" r="8"/><path d="M6 46h44M12 40h32v6H12z"/></svg>
      </div>
      <div class="step-title">ONE TWO HOUR VISIT</div>
      <div class="step-note">where your child will complete an MRI scan answer questions about their puberty stage have a small hair sample taken to study puberty hormones</div>
    </div>
  </section>

  <section class="eligible abs">
    <h3>YOUR CHILD MAY BE ELIGIBLE IF THEY :</h3>
    <ul>
      <li><svg width="18" height="18" viewBox="0 0 18 18" aria-hidden="true"><circle cx="9" cy="9" r="9" fill="var(--navy)"/><path d="M5 9l3 3 5-6" stroke="#fff" stroke-width="2" fill="none"/></svg>Are age 10-17</li>
      <li><svg width="18" height="18" viewBox="0 0 18 18" aria-hidden="true"><circle cx="9" cy="9" r="9" fill="var(--navy)"/><path d="M5 9l3 3 5-6" stroke="#fff" stroke-width="2" fill="none"/></svg>Tend to worry or overthink negative thoughts</li>
      <li><svg width="18" height="18" viewBox="0 0 18 18" aria-hidden="true"><circle cx="9" cy="9" r="9" fill="var(--navy)"/><path d="M5 9l3 3 5-6" stroke="#fff" stroke-width="2" fill="none"/></svg>Have not been diagnosed with psychosis, learning problems, or autism</li>
    </ul>
    <div class="scan" role="img" aria-label="Photo of an MRI scanner room in blue light with monitors showing brain scans"></div>
  </section>

  <section class="contact abs">
    <div class="contact-label">Please contact us</div>
    <div class="contact-ask">INTERESTED IN PARTICIPATING?<br>WANT MORE INFORMATION?</div>
    <div class="contact-mail">
      <svg width="26" height="20" viewBox="0 0 26 20" fill="none" stroke="currentColor" stroke-width="2" aria-hidden="true"><rect x="1" y="1" width="24" height="18" rx="2"/><path d="M1 2l12 10L25 2"/></svg>
      molvtstudy@halvernhealth.org
    </div>
  </section>

  <footer class="footer abs">
    <div class="org"><span class="org-mark"></span><span>Halvern Ridge<br>University</span></div>
    <div class="footer-rule"></div>
    <div class="url">www.research.halvernridge.edu</div>
  </footer>
</main>
</body>
</html>
```